looking to have a web site for the company which provides services in the industrial and commercial sectors such as: electrical, automation control and system integration, construction and maintenance, millwright, equipment assembly repair and installation. I have the domain already brivanholdings.net and logo. Most recent projects fulfilled for the following clients: MarlowKibbleCo, Dunholt University, OKSU, FALSTO, Tazzik, Prairie Grains

Target Market(s)

industrial and commercial sectors in electrical, automation, millwright and fabrication fields

Industry/Entity Type

Industrial

Coding

Coded - Design and coding required

Number of Pages Required

5+ page

Font styles to use
Sans Serif

Colors

Designer to choose colors to be used in the design.

Requirements
Nice to have
• looking to get something not complicated, nicely presented with minimum or no scrolling

```html
<!DOCTYPE html>
<html lang="en">
<head>
<meta charset="utf-8">
<title>Brivan Group – Fast Electrical Services</title>
<link rel="stylesheet" href="https://fonts.googleapis.com/css2?family=Lato:wght@400;700;900&family=Open+Sans:wght@400;600;700&display=swap">
<style>
:root{
  --blue:#168ad9;
  --blue-dark:#0f6fb3;
  --ink:#2a2a2a;
  --text:#555;
  --muted:#7a7a7a;
  --white:#fff;
  --dark:#262626;
  --footer:#2c2c2c;
  --line:#dcdcdc;
  --navy:#1d3a5c;
}
*{box-sizing:border-box;margin:0;padding:0}
html,body{width:1200px;height:3109px;overflow:hidden}
body{position:relative;background:var(--white);font-family:"Open Sans",Arial,sans-serif;color:var(--text)}
.abs{position:absolute}
.ph{position:absolute}

/* header */
.topbar{left:0;top:0;width:1200px;height:24px;background:#2b2b2b}
.hero{left:0;top:0;width:1200px;height:664px;background:linear-gradient(180deg,#5b6a70 0%,#8f9a9b 45%,#4a5357 100%)}
.hero-shade{left:0;top:0;width:1200px;height:664px;background:rgba(20,25,30,.35)}
.header-box{left:68px;top:24px;width:1066px;height:96px;background:var(--white)}
.brand{left:24px;top:26px;display:flex;align-items:center;gap:10px;font-family:"Lato",sans-serif;font-weight:900;font-size:34px;color:var(--blue);letter-spacing:1px}
.brand-mark{width:16px;height:16px;background:var(--blue)}
.contact{top:26px;display:flex;gap:10px;font-family:Arial,sans-serif;font-size:14px;color:#444;line-height:20px}
.contact b{color:#333}
.contact svg{flex:none;margin-top:2px}
.nav{left:68px;top:120px;width:1066px;height:50px;background:var(--blue);display:flex;align-items:center;padding-left:30px;gap:0}
.nav a{color:var(--white);font-family:"Lato",sans-serif;font-weight:700;font-size:14px;text-decoration:none;margin-right:58px}
.hero-title{left:0;top:326px;width:1200px;text-align:center;font-family:"Lato",sans-serif;font-weight:900;font-size:44px;color:var(--white)}
.hero-sub{left:0;top:380px;width:1200px;text-align:center;font-family:"Lato",sans-serif;font-weight:700;font-size:15px;color:var(--white)}

/* feature cards */
.band{left:0;top:664px;width:1200px;height:336px;background:var(--blue)}
.cards{left:68px;top:605px;width:1066px;height:357px;background:var(--white);display:flex}
.card{flex:1;padding:26px 20px 0;border-right:1px solid var(--line)}
.card:last-child{border-right:0}
.card-photo{width:298px;height:172px}
.card h3{margin-top:20px;font-family:Arial,sans-serif;font-weight:400;font-size:18px;color:#333;text-transform:uppercase}
.card p{margin-top:8px;font-size:14px;line-height:21px;color:var(--muted);width:290px}
.card .more{display:block;margin-top:20px;font-family:Arial,sans-serif;font-weight:700;font-size:14px;color:#333}

/* headings */
.kicker{position:absolute;font-family:"Lato",sans-serif;font-size:17px;color:#333;padding:12px 0 0 14px}
.kicker::before{content:"";position:absolute;left:0;top:0;width:40px;height:40px;border-left:2px solid var(--blue);border-top:2px solid var(--blue)}
.kicker.light{color:var(--white)}
.title{position:absolute;font-family:"Lato",sans-serif;font-weight:700;font-size:32px;color:var(--blue);letter-spacing:.5px}

/* about */
.about-text{left:68px;top:1150px;width:630px;font-family:Arial,sans-serif;font-size:13.6px;line-height:21px;color:#444}
.about-text p+p{margin-top:20px}
.about-frame{left:725px;top:1078px;width:410px;height:297px}

/* projects */
.projects{left:0;top:1472px;width:1200px;height:539px;background:linear-gradient(180deg,#2e2e2e,#1f1f1f)}
.tiles{left:68px;top:1617px;width:1066px;display:flex;gap:17px}
.tile{position:relative;width:254px;height:336px}
.tile .ph{left:0;top:0;width:254px;height:282px}
.tile-label{position:absolute;left:0;bottom:0;width:254px;height:54px;background:rgba(20,20,20,.85);color:var(--white);font-family:"Lato",sans-serif;font-weight:700;font-size:22px;display:flex;align-items:center;justify-content:center}

/* testimonials */
.quote-mark{left:74px;top:2222px}
.quote-text{left:134px;top:2248px;width:380px;font-size:12.5px;line-height:23px;color:#555}
.quote-text b{color:#444;font-weight:600}
.avatar{left:134px;top:2394px;width:84px;height:84px;border-radius:50%;background:#8a8f96}
.person{left:232px;top:2414px;font-size:15px;color:#555}
.person small{display:block;font-size:12.5px;font-style:italic;color:var(--navy);margin-top:2px}
.pager{left:508px;top:2516px;display:flex;gap:6px}
.pager span{width:30px;height:26px;border:1px solid #ccc;display:flex;align-items:center;justify-content:center}
.faq{left:610px;width:507px;border:1px solid var(--line);display:flex;align-items:flex-start}
.faq-icon{width:46px;height:44px;background:var(--blue);display:flex;align-items:center;justify-content:center;flex:none}
.faq-q{padding:12px 0 0 34px;font-size:13.4px;font-weight:700;color:var(--navy)}
.faq.open{border-color:#e2e2e2;height:118px}
.faq.open .faq-icon{background:transparent}
.faq.open .faq-q{padding-left:2px}
.faq.open p{margin-top:6px;font-weight:400;font-size:12.5px;line-height:21px;color:#9a9a9a;width:360px}

/* footer */
.footer{left:0;top:2622px;width:1200px;height:433px;background:var(--footer)}
.f-title{position:absolute;font-family:"Lato",sans-serif;font-size:17px;color:var(--blue);text-transform:uppercase}
.f-text{left:68px;width:250px;font-size:12.5px;line-height:21px;color:#d8d8d8}
.f-photo{left:68px;top:2869px;width:250px;height:116px}
.f-list{list-style:none;font-size:12.5px;color:#d8d8d8}
.f-list li{height:27px}
.f-list li::before{content:"›";margin-right:8px;color:#bbb}
.social{left:414px;top:2935px;display:flex;gap:8px}
.social span{width:42px;height:42px;border:1px solid #bbb;display:flex;align-items:center;justify-content:center}
.social span i{width:8px;height:8px;background:#ddd;display:block}
.f-contact{left:837px;display:flex;align-items:center;gap:14px;font-size:13px;color:#e6e6e6;line-height:19px}
.f-brand{left:850px;top:2892px;display:flex;align-items:center;gap:10px;font-family:"Lato",sans-serif;font-weight:900;font-size:34px;color:#9a9a9a;letter-spacing:1px}
.f-brand i{width:16px;height:16px;background:#9a9a9a;display:block}
.bottom{left:0;top:3055px;width:1200px;height:54px;background:var(--blue);color:var(--white);font-size:13px;display:flex;align-items:center;justify-content:space-between;padding:0 66px 0 70px}
.bottom nav span{margin:0 6px}
</style>
</head>
<body>

<!-- hero -->
<div class="ph hero" role="img" aria-label="Industrial grain silos and plant towers under an overcast sky"></div>
<div class="abs hero-shade"></div>
<div class="abs topbar"></div>

<header class="abs header-box">
  <div class="abs brand"><span class="brand-mark"></span>BRIVAN GROUP</div>
  <div class="abs contact" style="left:577px">
    <svg width="22" height="22" viewBox="0 0 22 22"><circle cx="11" cy="11" r="9" fill="none" stroke="#168ad9" stroke-width="2"/><ellipse cx="11" cy="11" rx="4" ry="9" fill="none" stroke="#168ad9" stroke-width="1.5"/><line x1="2" y1="11" x2="20" y2="11" stroke="#168ad9" stroke-width="1.5"/></svg>
    <div><b>Brivan Group Pvt. Ltd.</b><br>412 Foundry Park Phase III</div>
  </div>
  <div class="abs contact" style="left:820px">
    <svg width="22" height="22" viewBox="0 0 22 22"><circle cx="11" cy="11" r="10" fill="#168ad9"/><path d="M7 6c1 0 2 2 2 3s-1 1-1 2 2 3 3 3 1-1 2-1 3 1 3 2-1 2-2 2c-4 0-9-5-9-9 0-1 1-2 2-2z" fill="#fff"/></svg>
    <div><b>CALL US:</b> +(321) 55 204 118<br>mail@fieldworkpress.com</div>
  </div>
</header>

<nav class="abs nav">
  <a>HOME</a><a>SERVICES</a><a>PROJECT</a><a>NEW</a><a>CONTACT US</a>
</nav>

<h1 class="abs hero-title">FAST ELECTRICAL SERVICES!</h1>
<p class="abs hero-sub">"WE PROVIDE RELIABLE AND AFFORDABLE SERVICES"</p>

<!-- feature cards -->
<div class="abs band"></div>
<section class="abs cards">
  <article class="card">
    <div class="card-photo" role="img" aria-label="Worker holding a blue hard hat in a factory hall" style="background:linear-gradient(135deg,#1f5fa8,#9fb4c6)"></div>
    <h3>Technology &amp; Innovation</h3>
    <p>We also understand that the safety of your family comes first.</p>
    <span class="more">READ MORE</span>
  </article>
  <article class="card">
    <div class="card-photo" role="img" aria-label="Two engineers in safety vests shaking hands at a plant" style="background:linear-gradient(135deg,#8a98a6,#c8d23a 60%,#6c7884)"></div>
    <h3>Our Operations</h3>
    <p>We also understand that the safety of your family comes first.</p>
    <span class="more">READ MORE</span>
  </article>
  <article class="card">
    <div class="card-photo" role="img" aria-label="Team of workers in hard hats gathered in a circle" style="background:linear-gradient(135deg,#c9a46a,#6a7f9a 60%,#e0c040)"></div>
    <h3>Great Teamwork</h3>
    <p>We also understand that the safety of your family comes first.</p>
    <span class="more">READ MORE</span>
  </article>
</section>

<!-- about -->
<div class="kicker" style="left:70px;top:1058px">WELCOME</div>
<h2 class="title" style="left:82px;top:1096px">ABOUT US</h2>
<div class="abs about-text">
  <p>Lorem Ipsum is simply dummy text &nbsp;is a leading manufacturer &amp; exporter of flat power transmission belts &amp; Roller Coverings. We are an ISO 9001:2008 certified company focusing on offering high Performance products with consistent &amp; reliable properties at most economical prices. Based on our Performance we have been awarded Export House Status by Government of India. We have setup a state art of the manufacturing facility for efficient production processes with inbuilt quality checks.</p>
  <p>Our products include tangential belts &amp; spindle tapes, flat transmission belts, folder gluer belts, machine tapes, leather belts, rough top belting, knitting machine belts, condenser tapes, roller coverings, rubber fillets, rubber emery, rubberized fabrics, coated chrome leather rolls, belting tools &amp; accessories.</p>
</div>
<svg class="abs about-frame" viewBox="0 0 410 297" aria-hidden="true">
  <polygon points="0,40 0,297 410,297 390,283 14,283 14,40" fill="#168ad9"/>
  <polygon points="330,0 390,0 390,100" fill="#168ad9"/>
  <polygon points="14,0 390,0 390,283 14,283" fill="none"/>
</svg>
<div class="ph" role="img" aria-label="Stainless steel process machinery with control cabinet" style="left:748px;top:1085px;width:358px;height:262px;background:linear-gradient(135deg,#7b8790,#c4ccd2 50%,#5e6a73);border:6px solid #fff"></div>

<!-- projects -->
<section class="ph projects" role="img" aria-label="Dim background of industrial pipework"></section>
<div class="kicker light" style="left:70px;top:1508px">OUR LATEST</div>
<h2 class="title" style="left:82px;top:1540px">PROJECTS</h2>
<div class="abs tiles">
  <div class="tile"><div class="ph" role="img" aria-label="White high-rise apartment tower against blue sky" style="background:linear-gradient(180deg,#bcd4ea,#e8eef3 60%,#9fb0c0)"></div><div class="tile-label">INDUSTRIAL</div></div>
  <div class="tile"><div class="ph" role="img" aria-label="Tower with greenery on every balcony" style="background:linear-gradient(180deg,#7fa9d8,#5d8a3d 50%,#8aa36a)"></div><div class="tile-label">COMMERCIAL</div></div>
  <div class="tile"><div class="ph" role="img" aria-label="Red brick terraced houses" style="background:linear-gradient(180deg,#7fa9d8,#a45a45 50%,#7a8a6a)"></div><div class="tile-label">INDUSTRIAL</div></div>
  <div class="tile"><div class="ph" role="img" aria-label="White high-rise apartment tower against blue sky" style="background:linear-gradient(180deg,#bcd4ea,#e8eef3 60%,#9fb0c0)"></div><div class="tile-label">INDUSTRIAL</div></div>
</div>

<!-- testimonials & faq -->
<div class="kicker" style="left:70px;top:2066px">OUR LATEST</div>
<h2 class="title" style="left:82px;top:2100px">TESTIMONIALS &amp; FAQ</h2>

<svg class="abs quote-mark" width="26" height="20" viewBox="0 0 26 20"><path d="M0 20V11C0 5 3 1 9 0v4c-3 1-4 3-4 6h4v10zM15 20V11c0-6 3-10 9-11v4c-3 1-4 3-4 6h4v10z" fill="#168ad9"/></svg>
<p class="abs quote-text">Far far away, <b>behind</b> the word mountains, far from the countries <b>Vokalia and Conso</b>nantia, there live the blinds and Separated they live in Bookmarksgrove right at the coast of the Semantics, language ocean. A small river named Duden flows their place and it with the necessary regelialia. It is a country.</p>
<div class="ph avatar" role="img" aria-label="Portrait of the client"></div>
<div class="abs person">Daniel Orwin<small>Chairman, Hestmark Company LTD.</small></div>
<div class="abs pager">
  <span><svg width="8" height="10" viewBox="0 0 8 10"><path d="M6 1 2 5l4 4" fill="none" stroke="#666" stroke-width="1.5"/></svg></span>
  <span><svg width="8" height="10" viewBox="0 0 8 10"><path d="M2 1l4 4-4 4" fill="none" stroke="#666" stroke-width="1.5"/></svg></span>
</div>

<div class="abs faq" style="top:2218px">
  <span class="faq-icon"><svg width="18" height="18" viewBox="0 0 18 18"><circle cx="9" cy="9" r="8" fill="#fff"/><path d="M6 9h6M9 6l3 3-3 3" fill="none" stroke="#168ad9" stroke-width="1.8"/></svg></span>
  <div class="faq-q">How can we find proper consultant for our business?</div>
</div>
<div class="abs faq" style="top:2282px">
  <span class="faq-icon"><svg width="18" height="18" viewBox="0 0 18 18"><circle cx="9" cy="9" r="8" fill="#fff"/><path d="M6 9h6M9 6l3 3-3 3" fill="none" stroke="#168ad9" stroke-width="1.8"/></svg></span>
  <div class="faq-q">What is the main sourch of the business of Tovard Company?</div>
</div>
<div class="abs faq" style="top:2347px">
  <span class="faq-icon"><svg width="18" height="18" viewBox="0 0 18 18"><circle cx="9" cy="9" r="8" fill="#fff"/><path d="M6 9h6M9 6l3 3-3 3" fill="none" stroke="#168ad9" stroke-width="1.8"/></svg></span>
  <div class="faq-q">Why should we press Get a Quote button?</div>
</div>
<div class="abs faq open" style="top:2413px">
  <span class="faq-icon"><svg width="18" height="18" viewBox="0 0 18 18"><circle cx="9" cy="9" r="8" fill="#168ad9"/><path d="M6 9h6M9 6l3 3-3 3" fill="none" stroke="#fff" stroke-width="1.8"/></svg></span>
  <div class="faq-q">How can we find proper consultant for our business?
    <p>Lorem ipsum dolor sit amet, consectetur adipiscing elit, sed do eiusmod tempor incididunt ut labore et dolore Ut enim ad minim veniam.</p>
  </div>
</div>

<!-- footer -->
<footer class="abs footer"></footer>
<h4 class="f-title" style="left:68px;top:2666px">About Us</h4>
<p class="abs f-text" style="top:2704px">Over 15 years of experience in all industry branches we've built well known name Our solutions</p>
<p class="abs f-text" style="top:2790px">Our solutions are used in over 150 and countries supporting millions of customers in domain of electricity, construction,</p>
<div class="ph f-photo" role="img" aria-label="Group of smiling workers in hard hats" style="background:linear-gradient(135deg,#e9e4d8,#d9b84a 50%,#8c6f55)"></div>

<h4 class="f-title" style="left:410px;top:2666px">Discover</h4>
<ul class="abs f-list" style="left:414px;top:2707px">
  <li>About us</li><li>FAQ</li><li>Quotation</li><li>Contacts</li><li>Shop</li><li>Terms and condition</li>
</ul>
<ul class="abs f-list" style="left:614px;top:2707px">
  <li>Shortcircuit Repaire</li><li>Faulty And Old Wiring</li><li>Poor Maintenance</li><li>Electrical Maintenace</li><li>Install And Upgrate</li><li>Dianosis And Repaire</li>
</ul>
<h4 class="f-title" style="left:410px;top:2896px">Social Media</h4>
<div class="abs social" aria-label="Social media links">
  <span><i></i></span><span><i></i></span><span><i></i></span>
</div>

<h4 class="f-title" style="left:837px;top:2666px">Upcoming Exhibition</h4>
<div class="abs f-contact" style="top:2717px">
  <svg width="26" height="26" viewBox="0 0 26 26"><circle cx="13" cy="13" r="13" fill="#168ad9"/><path d="M13 6a5 5 0 0 0-5 5c0 4 5 9 5 9s5-5 5-9a5 5 0 0 0-5-5z" fill="#fff"/><circle cx="13" cy="11" r="2" fill="#168ad9"/></svg>
  <div>Lindenhofweg 52<br>4410 Halden</div>
</div>
<div class="abs f-contact" style="top:2770px">
  <svg width="26" height="26" viewBox="0 0 26 26"><circle cx="13" cy="13" r="13" fill="#168ad9"/><path d="M9 8c1 0 2 2 2 3s-1 1-1 2 2 3 3 3 1-1 2-1 3 1 3 2-1 2-2 2c-4 0-9-5-9-9 0-1 1-2 2-2z" fill="#fff"/></svg>
  <div>+41 55 208 47 19</div>
</div>
<div class="abs f-contact" style="top:2807px">
  <svg width="26" height="26" viewBox="0 0 26 26"><circle cx="13" cy="13" r="13" fill="#168ad9"/><rect x="7" y="9" width="12" height="9" fill="#fff"/><path d="M7 9l6 5 6-5" fill="none" stroke="#168ad9" stroke-width="1.3"/></svg>
  <div>info@brivanholdings.net</div>
</div>
<div class="abs f-brand"><i></i>BRIVAN GROUP</div>

<div class="abs bottom">
  <nav>Home<span>|</span>About us<span>|</span>Products<span>|</span>Enquiry<span>|</span>Contact Us</nav>
  <div>© 2017 www.brivanholdings.net/ , All Rights Reserved</div>
</div>

</body>
</html>
```